ultra-minimalist business card

front (black background, matte):

tarik b. hosseny
writer | photographer
get@tarikhosseny.com

back (white background, matte):

a picture speaks a thousand words;
a word draws a thousand pictures.

www.tarikhosseny.com

all text should be small (white or silver - as long as it shows against the black - on the front; black or gray - as long as it shows against the white - on the back).

feel free to get creative in terms of arrangement, alignment, and font type, but remember, the overall style is minimalist, so nothing too fancy, please.

thanks.

```html
<!DOCTYPE html>
<html lang="en">
<head>
<meta charset="utf-8">
<title>Tarik B. Hosseny — Business Card</title>
<link href="https://fonts.googleapis.com/css2?family=Montserrat:wght@500;600&family=Arimo&family=Questrial&display=swap" rel="stylesheet">
<style>
  :root {
    --stage: #b3b3b3;
    --ink: #231f20;
    --paper: #ffffff;
    --text-dark: #333333;
  }
  * { box-sizing: border-box; margin: 0; padding: 0; }
  html, body {
    width: 1200px; height: 428px; overflow: hidden;
    background: var(--stage);
  }
  .stage { position: relative; width: 1200px; height: 428px; }
  .card {
    position: absolute; top: 69px; width: 464px; height: 283px;
    background: var(--paper); overflow: hidden;
    box-shadow: 3px 4px 6px rgba(0,0,0,0.25);
  }
  .card--front { left: 79px; }
  .card--back { left: 639px; }

  .band { position: absolute; left: 0; width: 100%; }
  .band--header { top: 0; height: 119px; background: var(--ink); }
  .band--quote { top: 119px; height: 97px; background: var(--paper); }
  .band--footer { top: 216px; height: 67px; background: var(--ink); }

  .identity {
    position: absolute; inset: 0;
    display: flex; align-items: center; justify-content: center; gap: 12px;
  }
  .identity__mark { width: 58px; height: 58px; flex: none; }
  .identity__text { color: var(--paper); font-family: "Montserrat", sans-serif; }
  .identity__name {
    font-weight: 600; font-size: 27px; line-height: 1; letter-spacing: 0.2px;
    padding-bottom: 5px; border-bottom: 3px solid var(--paper);
    white-space: nowrap;
  }
  .identity__role {
    font-weight: 500; font-size: 15.5px; margin-top: 5px; letter-spacing: 0.3px;
    white-space: nowrap;
  }

  .quote {
    position: absolute; inset: 0;
    display: flex; align-items: center; justify-content: center;
    font-family: "Arimo", sans-serif; font-size: 17px; line-height: 24px;
    color: var(--text-dark); text-align: center; padding-bottom: 4px;
  }

  .contact {
    position: absolute; inset: 0;
    display: flex; align-items: center; justify-content: center;
    font-family: "Questrial", sans-serif; font-size: 14.5px;
    color: var(--paper); padding-top: 17px; white-space: nowrap;
  }
  .contact__sep { margin: 0 7px; }

  .website {
    position: absolute; left: 0; right: 0; top: 128px;
    text-align: center;
    font-family: "Arimo", sans-serif; font-weight: 700; font-size: 20px;
    color: var(--text-dark); text-decoration: underline; text-underline-offset: 3px;
  }
</style>
</head>
<body>
<main class="stage">
  <section class="card card--front" aria-label="Card front">
    <div class="band band--header">
      <div class="identity">
        <svg class="identity__mark" viewBox="0 0 58 58" aria-hidden="true">
          <circle cx="29" cy="29" r="27" fill="#ffffff"/>
        </svg>
        <div class="identity__text">
          <div class="identity__name">TARIK B. HOSSENY</div>
          <div class="identity__role">WRITER &amp; PHOTOGRAPHER</div>
        </div>
      </div>
    </div>
    <div class="band band--quote">
      <p class="quote">“a picture speaks a thousand words;<br>a word draws a thousand pictures”</p>
    </div>
    <div class="band band--footer">
      <p class="contact">get@tarikhosseny.com<span class="contact__sep">|</span>www.tarikhosseny.com</p>
    </div>
  </section>

  <section class="card card--back" aria-label="Card back">
    <p class="website">www.tarikhosseny.com</p>
  </section>
</main>
</body>
</html>
```